Moderne CI für einen Immobilienmakler [www.hefner-wohnwerte.de]
Zielgruppe
Kunden für hochwertige Immobilien, also gemischtes eher anspruchvolles Klientel.
Hallo,
ich betreibe ein junges Immobilienunternehmen im 4. Geschäftsjahr. Wir vermarkten ausschließlich hochwertige Immobilien. Meine derzeitiges Logo habe ich damals selbst entworfen und es harmoniert gut mit meiner Website [www.hefner-wohnwerte.de] leider habe ich für Printmedien nie eine CI hinbekommen die mir richtig gefällt und die im Gesamt- und Farbkonzept zu meinem Onlineauftritt passt.
Ich wünsche mir nun von einem professionellen Designer eine modern- edle CI mit Entwürfen für Briefpapier, Umschläge C4 und DL, A4 Exposé-Mappe sowie die Rohlinge für eine Dreiseiter Image-Broschüre, für ein Objekt Expose sowie für eine Print-Annonce.
Eine spätere Zusammenarbeit für weitere Medien ist erwünscht.

```html
<!DOCTYPE html>
<html lang="de">
<head>
<meta charset="utf-8">
<title>Hefner Wohnwerte – Exposé und Visitenkarten</title>
<link rel="stylesheet" href="https://fonts.googleapis.com/css2?family=Arimo:wght@400;700&display=swap">
<style>
  :root{
    --red:#d6101f;
    --ink:#3a3a3a;
    --grey:#8a8a8a;
    --frame:#9a9a9a;
    --paper:#ffffff;
    --paper-fade:#dcdcdc;
    --stage:#e6e4e0;
  }
  *{box-sizing:border-box;margin:0;padding:0}
  html,body{width:1200px;height:1200px;overflow:hidden}
  body{background:var(--stage);font-family:"Arimo",Arial,sans-serif;color:var(--ink);position:relative}

  .wordmark{position:absolute;font-weight:400;color:var(--grey);letter-spacing:-0.5px;white-space:nowrap;display:flex;align-items:center;gap:10px}
  .wordmark::after{content:"";width:.32em;height:.32em;background:var(--red)}

  /* Exposé sheet */
  .expose{position:absolute;left:37px;top:37px;width:795px;height:1125px;overflow:hidden;
    background:linear-gradient(180deg,var(--paper) 0%,var(--paper) 45%,var(--paper-fade) 100%);
    box-shadow:0 4px 14px rgba(0,0,0,.25)}
  .expose .wordmark{right:37px;top:95px;font-size:31px}
  .headline{position:absolute;left:37px;top:262px;font-size:19px;font-weight:400;color:var(--grey)}
  .headline .sep{color:var(--red);margin:0 4px}
  .headline .sub{color:var(--ink)}

  .photo{position:absolute;border:6px solid var(--frame)}
  .photo-main{left:37px;top:300px;width:483px;height:325px;
    background:linear-gradient(180deg,#6fa3d8 0%,#cfe0ef 40%,#8aa56a 65%,#4f6f38 100%)}
  .photo-a{left:538px;top:658px;width:224px;height:115px;
    background:linear-gradient(180deg,#9fc0e0 0%,#c85a5a 55%,#8d8d8d 100%)}
  .photo-b{left:538px;top:784px;width:224px;height:115px;
    background:linear-gradient(180deg,#f2f2f2 0%,#dcdcdc 60%,#b88a5c 100%)}
  .photo-c{left:538px;top:909px;width:224px;height:115px;
    background:linear-gradient(180deg,#f4f4f4 0%,#cfcfcf 55%,#4a4a4a 100%)}

  .details{position:absolute;left:533px;top:298px}
  .details-title{font-size:11px;color:var(--grey);display:flex;align-items:center;gap:6px}
  .details-title::before{content:"";border-left:5px solid transparent;border-right:5px solid transparent;border-top:7px solid var(--red)}
  .details ul{list-style:none;margin-top:14px}
  .details li{font-size:14px;font-weight:700;color:var(--ink);border-left:3px solid var(--red);
    padding-left:12px;height:21px;line-height:21px;margin-bottom:11px}
  .details sup{font-size:9px;line-height:0;vertical-align:6px}

  .copy{position:absolute;top:655px;width:232px;font-size:13.5px;line-height:20.5px;color:var(--ink);hyphens:auto}
  .copy p{margin-bottom:20px}
  .copy-left{left:37px}
  .copy-right{left:289px}

  .footer{position:absolute;left:37px;top:1057px;font-size:11px;line-height:15px;color:var(--grey);white-space:nowrap}
  .footer .col{position:absolute;top:0}
  .footer .col1{left:0}
  .footer .col2{left:203px}
  .footer .col3{left:473px}
  .footer .rule{position:absolute;top:0;width:2px;height:48px;background:var(--red)}
  .footer .rule-1{left:143px}
  .footer .rule-2{left:413px}
  .footer .brand b{color:var(--ink)}
  .footer .brand span{color:var(--red)}

  /* Business cards */
  .card{position:absolute;width:363px;height:232px;background:linear-gradient(180deg,#fff 0%,#fff 55%,#e4e4e4 100%);
    box-shadow:0 3px 10px rgba(0,0,0,.28)}
  .card-front{left:800px;top:540px}
  .card-front .wordmark{right:28px;top:70px;font-size:27px}
  .card-back{left:800px;top:811px}
  .contact{position:absolute;left:182px;top:51px;font-size:12px;line-height:16px;color:var(--ink);white-space:nowrap}
  .contact .name{font-weight:700;font-size:14.5px;line-height:17px}
  .contact .role{color:var(--grey);font-size:11px;margin-bottom:12px}
  .contact .addr{margin-bottom:12px}
  .contact dl{display:grid;grid-template-columns:40px auto;column-gap:8px;margin-left:-48px}
  .contact dl.gap{margin-top:10px}
  .contact dt{text-align:right}
</style>
</head>
<body>

<section class="expose">
  <div class="wordmark">hefner wohnwerte</div>

  <h1 class="headline">Marburg-Kernstadt<span class="sep">|</span><span class="sub">Neubau Architektenhäuser</span></h1>

  <div class="photo photo-main" role="img" aria-label="Foto: moderne Architektenhäuser mit Terrassen am Hang, Blick über grüne Hügel"></div>

  <aside class="details">
    <div class="details-title">Objekt details</div>
    <ul>
      <li>Hochwertige Einfamilienhäuser</li>
      <li>220 m<sup>2</sup> Wohnfläche</li>
      <li>Niedrigenergiebauweise</li>
      <li>Dachterrasse und Garten</li>
      <li>Bezugsfertig Ende 2009</li>
      <li>Preis 485. 000.- Euro</li>
    </ul>
  </aside>

  <div class="copy copy-left">
    <p>Neubau-Ensemble von vier architek&shy;tonisch hochwertigen Einfamilienhäu&shy;sern in einer der schönsten Wohn&shy;lagen Marburgs.</p>
    <p>Die exklusiven Wohnhäuser werden in Niedrigenergiebauweise ausge&shy;führt und durch Erdwärmepumpen in Verbindung mit Fußbodenheizung beheizt. Die Ausführung im Innenaus&shy;bau ist individuell hochwertig und wird Sie begeistern.</p>
    <p>Lichtdurchflutete Räume, sonnige Gärten und Dachterrassen laden zum Verweilen ein - oder zum Arbeiten wenn es sich nicht vermeiden lässt.</p>
  </div>
  <div class="copy copy-right">
    <p>Der Kaufpreis eines schlüsselferti&shy;gen Wohnhauses mit bis zu 220 m² Wohnfläche beträgt 485.000,- Euro. Reservierungen können ab Bauan&shy;tragsgenehmigung, vor Mitte Juni entgegengenommen werden.</p>
    <p>Der Bezug der Häuser ist für Ende 2009 – Beginn 2010 vorgesehen.</p>
  </div>

  <div class="photo photo-a" role="img" aria-label="Foto: Häuserzeile mit roter Fassade und Carport"></div>
  <div class="photo photo-b" role="img" aria-label="Foto: heller Wohnraum mit bodentiefen Fenstern und Parkett"></div>
  <div class="photo photo-c" role="img" aria-label="Foto: modernes Bad mit dunklen Fliesen"></div>

  <footer class="footer">
    <div class="col col1">
      <div class="brand">Hefner <span>|</span> <b>Wohnwerte</b></div>
      Lindenweg 14<br>D-35039 Marburg
    </div>
    <div class="rule rule-1"></div>
    <div class="col col2">
      Telefon: +49 (0)6421-5523410<br>
      Telefax: +49 (0)6421-5523412<br>
      E-Mail: info@hefner-wohnwerte.de
    </div>
    <div class="rule rule-2"></div>
    <div class="col col3">
      Immobilienmakler gem. §34c GewO<br>
      Steuernummer: 03167250918 Finanzamt Marburg<br>
      Verantwortlicher gemäss § 6 MDStV: Markus Hefner
    </div>
  </footer>
</section>

<section class="card card-front">
  <div class="wordmark">hefner wohnwerte</div>
</section>

<section class="card card-back">
  <div class="contact">
    <div class="name">Markus Hefner</div>
    <div class="role">Immobilienmakler</div>
    <div class="addr">Lindenweg 14<br>D - 35039 Marburg</div>
    <dl>
      <dt>tel.:</dt><dd>+49 (0)6421 5523410</dd>
      <dt>fax:</dt><dd>+49 (0)6421 5523412</dd>
    </dl>
    <dl class="gap">
      <dt>e-mail:</dt><dd>info@hefner-wohnwerte.de</dd>
      <dt>web:</dt><dd>www.hefner-wohnwerte.de</dd>
    </dl>
  </div>
</section>

</body>
</html>
```